Tavorly - Landing Page

Need a landing page for a journal app. The app is based on a retrospective board, where each journal entry is split into 3 sections: "What went well", "What Didn't Go Well" and "Things To Try".
The landing page should match the style of all modern web application landing pages. Think Brimo, Quenta, Vexadro. I've included screenshots of the app.
One feature that I want to highlight that is not ready yet, is an AI coach. It will offer insights based on the history of the user's journal entries
1 page

```html
<!DOCTYPE html>
<html lang="en">
<head>
<meta charset="utf-8">
<title>Tavorly – Journal App</title>
<link rel="stylesheet" href="https://fonts.googleapis.com/css2?family=Plus+Jakarta+Sans:wght@300;400;500;600;700;800&family=Inter:wght@400;500;600&display=swap">
<style>
:root{
  --blue:#0f5fae;
  --blue-bright:#1877d2;
  --navy:#083577;
  --ink:#1d1f24;
  --text:#55595f;
  --muted:#8a8f96;
  --line:#e4e7ec;
  --soft:#f1f2f4;
  --dark-btn:#2a2b2e;
  --green:#1cc36b;
  --white:#fff;
}
*{margin:0;padding:0;box-sizing:border-box}
html,body{width:1200px;height:4213px;overflow:hidden}
body{position:relative;background:var(--white);font-family:"Plus Jakarta Sans",sans-serif;color:var(--ink)}
.abs{position:absolute}
.accent{color:var(--blue-bright);font-weight:800}
.btn{display:inline-flex;align-items:center;justify-content:center;background:var(--blue);color:var(--white);font-size:13px;font-weight:500;border-radius:3px;height:40px;padding:0 26px}
.btn.dark{background:var(--dark-btn)}

/* header */
.brand{display:flex;align-items:center;gap:8px;font-weight:700;font-size:16px;color:var(--blue)}
.brand .mark{width:30px;height:30px;background:var(--blue);border-radius:4px}
.nav-right{right:95px;top:20px;display:flex;align-items:center;gap:20px;font-size:11px}
.nav-right .login{display:flex;align-items:center;gap:6px;color:var(--ink)}
.nav-right .signup{background:var(--blue);color:#fff;padding:8px 12px;border-radius:3px;font-size:11px}

/* hero */
.hero{left:0;top:0;width:1200px;height:667px;overflow:hidden;
  background:
   linear-gradient(to bottom,#fff 0,rgba(255,255,255,0) 40%),
   repeating-linear-gradient(0deg,rgba(24,119,210,.07) 0 1px,transparent 1px 34px),
   repeating-linear-gradient(90deg,rgba(24,119,210,.07) 0 1px,transparent 1px 34px),
   linear-gradient(180deg,#fff 0,#f2f6fd 60%,#e7eefb 100%)}
.eyebrow{font-size:10px;letter-spacing:5px;color:var(--blue-bright);font-weight:500;text-align:center;width:100%}
.hero h1{top:118px;width:100%;text-align:center;font-weight:300;font-size:45px;line-height:48px}
.hero h1 b{font-weight:800}
.hero .sub{top:224px;width:100%;text-align:center;font-size:13px;color:var(--text)}
.hero .ctas{top:263px;width:100%;display:flex;justify-content:center;gap:10px}
.robot-area{left:860px;top:255px;width:240px;height:300px;border-radius:18px;
  background:linear-gradient(160deg,#f4f7fc 0%,#dfe6f1 55%,rgba(223,230,241,0) 100%)}
.ribbon{left:985px;top:480px;width:150px;height:44px;background:var(--blue-bright);color:#fff;transform:rotate(-14deg);
  display:flex;flex-direction:column;align-items:center;justify-content:center;font-weight:700;line-height:1.1}
.ribbon small{font-size:10px}
.ribbon span{font-size:17px}

.device{left:213px;top:400px;width:757px;height:290px;background:#fff;border:10px solid #eef1f6;border-bottom:0;border-radius:22px 22px 0 0;overflow:hidden}
.device .rail{position:absolute;left:0;top:0;width:30px;height:100%;background:#1f2733}
.device .rail i{display:block;width:10px;height:8px;background:#8893a3;margin:14px auto 0;border-radius:2px}
.device .rail i:first-child{background:var(--green)}
.device .entry{position:absolute;left:80px;top:22px;font-size:10px;font-weight:700}
.device .date{position:absolute;left:80px;top:44px;font-size:7px;display:flex;gap:8px;align-items:center}
.device .pill{background:var(--green);color:#fff;border-radius:8px;padding:1px 7px;font-size:6px}
.mini{position:absolute;top:70px;width:182px;height:220px;border:1px solid var(--line);border-radius:4px;font-size:6px;padding:6px 8px}
.mini h5{font-size:6.5px;font-weight:500;margin-bottom:12px}
.mini .tb{color:#555;margin-bottom:4px}
.mini ul{border:1px solid var(--line);padding:8px 8px 8px 16px;line-height:1.35;font-size:6.5px}

/* feature rows */
.feat h2{font-size:31px;font-weight:300}
.feat p{font-size:11.5px;line-height:19px;color:var(--text);margin-top:12px}
.feat h6{font-size:12px;font-weight:700;margin-top:14px}
.feat .btn{margin-top:24px}
.card{background:#fff;border-radius:6px;box-shadow:0 4px 24px rgba(20,30,60,.13);overflow:hidden;font-family:"Inter",sans-serif}
.card .hd{display:flex;align-items:center;gap:10px;padding:12px 16px;font-size:12px;border-bottom:1px solid var(--line);height:48px}
.card .tools{padding:12px 16px 8px;font-size:11px;color:#333;background:#f8f9fa}
.card .tools .r1{display:flex;gap:13px;font-weight:600}
.card .tools .r2{display:flex;gap:10px;margin-top:6px;font-size:12px}
.card .body{margin:0 12px;border:1px solid var(--line);border-bottom:0;padding:14px 14px 0 24px;height:200px;overflow:hidden}
.card ul{font-size:14px;line-height:21px;list-style:none}
.card li{position:relative}
.card li::before{content:"•";position:absolute;left:-9px}

/* why */
.sec-title{width:100%;text-align:center;font-size:31px;font-weight:300}
.sec-sub{width:100%;text-align:center;font-size:11.5px;line-height:18px;color:var(--text)}
.why-card{top:2359px;width:290px;height:241px;border:1px solid var(--line);border-radius:8px;text-align:center;padding:0 28px;background:#fff}
.why-card.active{border:1.5px solid #8db8e8;box-shadow:0 6px 20px rgba(24,119,210,.12)}
.why-card h3{font-size:16px;font-weight:600;margin-top:72px}
.why-card p{font-size:12px;line-height:20px;color:var(--text);margin-top:12px}
.hex{top:2297px;width:114px;height:114px}
.why-note{top:2655px;width:100%;text-align:center;font-size:12.5px;line-height:23px;font-weight:600}
.why-note a{color:var(--blue-bright);font-weight:500;text-decoration:none}

/* testimonial */
.testi{left:0;top:2771px;width:1200px;height:577px;background:var(--soft)}
.quote-text{left:296px;top:2983px;width:730px;font-size:16.8px;line-height:24.5px;color:#4a4d52}
.divider{left:296px;top:3147px;width:759px;height:1px;background:#d7dadf}
.avatar{left:294px;top:3170px;width:86px;height:86px;border-radius:50%;background:radial-gradient(circle at 50% 40%,#8a6a55,#3a2a22)}
.who{left:400px;top:3194px}
.who b{font-size:23px;font-weight:500;color:#45484d;display:block}
.who span{font-size:14px;color:var(--muted)}
.pager{left:810px;top:3190px;display:flex;align-items:center;gap:12px;font-size:22px}
.pager .cur{font-weight:700}
.pager .tot{color:var(--muted)}

/* faq */
.faq{left:213px;top:3535px;width:775px;display:grid;grid-template-columns:380px 380px;column-gap:15px;row-gap:9px}
.faq div{height:40px;background:#fff;box-shadow:0 2px 8px rgba(0,0,0,.08);border-radius:3px;display:flex;align-items:center;justify-content:space-between;padding:0 22px;font-size:11px;font-weight:500}
.faq div::after{content:"⌄";color:#999;font-size:10px}

/* cta */
.cta{left:144px;top:3834px;width:912px;height:290px;background:var(--navy);border-radius:34px;color:#fff;text-align:center}
.cta .eb{margin-top:48px;font-size:9px;letter-spacing:5px;color:#8aa3c9}
.cta h2{font-size:30px;font-weight:400;margin-top:8px}
.cta h2 b{color:#3b95f0;font-weight:800}
.cta p{font-size:12px;line-height:19px;margin:16px auto 0;width:640px;color:#dfe6f2}
.cta .btn{width:636px;margin-top:20px;background:#1565c0;font-size:13px}

/* footer */
.copy{top:4168px;width:100%;text-align:center;font-size:9px;color:#444}
.social{left:906px;top:4165px;display:flex;gap:19px}
.social i{width:11px;height:11px;border-radius:50%;background:#333;display:block}
</style>
</head>
<body>

<header>
  <div class="abs brand" style="left:93px;top:18px"><span class="mark"></span>Tavorly</div>
  <nav class="abs nav-right">
    <span class="login"><svg width="11" height="11" viewBox="0 0 12 12" fill="none" stroke="#222"><circle cx="6" cy="4" r="2.5"/><path d="M1.5 11c0-2.5 2-4 4.5-4s4.5 1.5 4.5 4"/></svg>Login</span>
    <span class="signup">Sign Up</span>
  </nav>
</header>

<section class="abs hero">
  <p class="abs eyebrow" style="top:96px">REFLECT, LEARN, GROW</p>
  <h1 class="abs">Capture Your <b>Journey,</b> Empower<br><span class="accent">Your Growth</span></h1>
  <p class="abs sub">Turn your daily reflections into actionable insights with our AI-powered journal.</p>
  <div class="abs ctas"><span class="btn">Start Your Journey</span><span class="btn dark">Learn More</span></div>
  <div class="abs robot-area" role="img" aria-label="Illustration of a white robot AI coach waving from behind the app window"></div>
  <div class="abs ribbon"><small>AI FEATURE</small><span>COMING SOON</span></div>

  <div class="abs device">
    <div class="rail"><i></i><i></i><i></i><i></i></div>
    <div class="entry">Entry</div>
    <div class="date">▣ Thu Aug 22 2024 ⌄ <span class="pill">Gym</span></div>
    <div class="mini" style="left:80px"><h5>👍 What Went Well?</h5><div class="tb">Normal ⇕ &nbsp;B I U S ”</div><ul><li>Completed all scheduled workouts this week.</li><li>Increased bench press weight by 10 pounds.</li><li>Maintained consistent energy levels throughout sessions.</li></ul></div>
    <div class="mini" style="left:288px"><h5>⚠ What Didn't Go Well?</h5><div class="tb">Normal ⇕ &nbsp;B I U S ”</div><ul><li>Struggled with form on deadlifts, leading to lower back discomfort.</li><li>Missed two stretching sessions after workouts.</li><li>Skipped meal prep, resulting in inconsistent nutrition.</li></ul></div>
    <div class="mini" style="left:496px"><h5>⚗ Things To Try</h5><div class="tb">Normal ⇕ &nbsp;B I U S ”</div><ul><li>Focus on deadlift form by lowering the weight and reviewing proper technique.</li><li>Set reminders for post-workout stretching to prevent muscle tightness.</li><li>Dedicate Sunday evenings to meal prep to ensure a balanced diet.</li></ul></div>
  </div>
</section>

<!-- What went well -->
<section class="abs feat" style="left:141px;top:798px;width:400px">
  <h2>What Went <span class="accent">Well</span></h2>
  <p>Recognize and celebrate your daily wins, no matter how small. This section is your space to reflect on the positive aspects of your day—what went smoothly, what you accomplished, and what brought you joy. By focusing on the good, you reinforce behaviors and decisions that lead to success, helping to cultivate a mindset of gratitude and positivity.</p>
  <h6>Purpose:</h6>
  <p style="margin-top:10px">By consistently acknowledging what went well, you build momentum and motivation, making it easier to replicate these successes in the future.</p>
  <span class="btn" style="width:179px">Start Your Journey</span>
</section>
<div class="abs card" style="left:659px;top:798px;width:302px;height:289px">
  <div class="hd"><span style="color:#1877d2">👍</span>What Went Well?</div>
  <div class="tools"><div class="r1"><span style="font-weight:400">Normal &nbsp;⇕</span><span>B</span><i>I</i><u>U</u><s>S</s><span>”</span></div><div class="r2">☰ ☰ ⇤ ⇥ &nbsp;T<sub>x</sub></div></div>
  <div class="body"><ul><li>Completed all scheduled workouts this week.</li><li>Increased bench press weight by 10 pounds.</li><li>Maintained consistent energy levels throughout sessions.</li></ul></div>
</div>

<!-- What didn't go well -->
<div class="abs card" style="left:163px;top:1300px;width:300px;height:283px">
  <div class="hd"><span style="color:#1877d2">⚠</span>What Didn't Go Well?</div>
  <div class="tools"><div class="r1"><span style="font-weight:400">Normal &nbsp;⇕</span><span>B</span><i>I</i><u>U</u><s>S</s><span>”</span></div><div class="r2">☰ ☰ ⇤ ⇥ &nbsp;T<sub>x</sub></div></div>
  <div class="body"><ul><li>Struggled with form on deadlifts, leading to lower back discomfort.</li><li>Missed two stretching sessions after workouts.</li><li>Skipped meal prep, resulting in inconsistent nutrition.</li></ul></div>
</div>
<section class="abs feat" style="left:646px;top:1277px;width:400px">
  <h2>What Didn't <span class="accent">Go Well</span></h2>
  <p>Every day comes with its challenges, and this section is where you can candidly address them. Whether it's a task that didn't go as planned, a goal you missed, or a moment that didn't meet your expectations, writing about it here helps you confront the issue head-on. This reflection isn't about dwelling on failure but about identifying areas for improvement and learning.</p>
  <h6>Purpose:</h6>
  <p style="margin-top:10px">By documenting what didn't go well, you gain clarity on the root causes of problems and start thinking about solutions, turning setbacks into learning opportunities.</p>
  <span class="btn" style="width:179px">Start Your Journey</span>
</section>

<!-- Things to try -->
<section class="abs feat" style="left:141px;top:1768px;width:400px">
  <h2>Things To <span class="accent">Try</span></h2>
  <p>This section is your action plan for tomorrow. Based on your reflections, what changes can you make? What new strategies can you implement? Whether it's a new habit, a different approach to a recurring problem, or something entirely new, this is where you map out your path forward. The goal is to use your insights to foster growth and continuous improvement.</p>
  <h6>Purpose:</h6>
  <p style="margin-top:10px">Things To Try' helps you take proactive steps toward improvement, ensuring that your reflections lead to tangible changes. It's about creating a better tomorrow by learning from today.</p>
  <span class="btn" style="width:179px">Start Your Journey</span>
</section>
<div class="abs card" style="left:659px;top:1779px;width:301px;height:289px">
  <div class="hd"><span style="color:#1877d2">⚗</span>Things To Try</div>
  <div class="tools"><div class="r1"><span style="font-weight:400">Normal &nbsp;⇕</span><span>B</span><i>I</i><u>U</u><s>S</s><span>”</span></div><div class="r2">☰ ☰ ⇤ ⇥ &nbsp;T<sub>x</sub></div></div>
  <div class="body"><ul><li>Focus on deadlift form by lowering the weight and reviewing proper technique.</li><li>Set reminders for post-workout stretching to prevent muscle tightness.</li><li>Dedicate Sunday evenings to meal prep to ensure a balanced diet.</li></ul></div>
</div>

<!-- Why -->
<h2 class="abs sec-title" style="top:2178px">Why Our Journal <span class="accent">App?</span></h2>
<p class="abs sec-sub" style="top:2233px">Discover the advantages of our journal app, designed to make self-reflection and personal growth<br>seamless and effective. Here's how our app can transform your daily journaling practice:</p>

<div class="abs why-card" style="left:134px"><h3>Structured Reflection</h3><p>Our app's clear, segmented approach helps you systematically analyze your day, focusing on successes, challenges, &amp; actionable improvements.</p></div>
<div class="abs why-card active" style="left:455px"><h3>Future-Ready with AI</h3><p>Our upcoming AI Coach will offer personalized guidance based on your journal history, turning your reflections into actionable insights.</p></div>
<div class="abs why-card" style="left:775px"><h3>Encourages Positive Habits</h3><p>The app's design encourages you to maintain a journaling habit, which is key to long-term personal growth and success.</p></div>

<svg class="abs hex" style="left:222px" viewBox="0 0 114 114"><polygon points="57,4 103,30 103,84 57,110 11,84 11,30" fill="#0f4fa8" stroke="#0f4fa8" stroke-width="6" stroke-linejoin="round"/><path d="M37 72h40M42 40l15 30 15-30M64 38l8 10" stroke="#fff" stroke-width="2" fill="none"/></svg>
<svg class="abs hex" style="left:542px" viewBox="0 0 114 114"><polygon points="57,4 103,30 103,84 57,110 11,84 11,30" fill="#1766c4" stroke="#1766c4" stroke-width="6" stroke-linejoin="round"/><circle cx="57" cy="57" r="18" stroke="#fff" stroke-width="2" fill="none"/><ellipse cx="57" cy="57" rx="26" ry="10" stroke="#fff" stroke-width="1.5" fill="none"/><text x="57" y="62" fill="#fff" font-size="13" font-weight="700" text-anchor="middle" font-family="Inter,sans-serif">AI</text></svg>
<svg class="abs hex" style="left:862px" viewBox="0 0 114 114"><polygon points="57,4 103,30 103,84 57,110 11,84 11,30" fill="#0f4fa8" stroke="#0f4fa8" stroke-width="6" stroke-linejoin="round"/><g stroke="#fff" stroke-width="2" fill="none"><circle cx="57" cy="50" r="6"/><path d="M46 70c0-7 5-11 11-11s11 4 11 11"/><circle cx="38" cy="60" r="5"/><circle cx="76" cy="60" r="5"/><rect x="51" y="32" width="12" height="7"/><path d="M49 78h16"/></g></svg>

<p class="abs why-note">Experience the benefits of a well-structured, user-friendly journaling tool that supports your<br>journey towards self-improvement and <a>personal achievement</a>.</p>

<!-- Testimonial -->
<section class="abs testi"></section>
<h2 class="abs sec-title" style="top:2844px">What Our Users <span class="accent">Say</span></h2>
<p class="abs sec-sub" style="top:2897px">Our users share their stories of how the app has transformed their reflection process<br>and supported their personal growth.</p>
<svg class="abs" style="left:140px;top:2977px" width="72" height="48" viewBox="0 0 72 48"><rect width="72" height="48" fill="#e8ebee"/><path d="M12 10h18v18l-8 12h-8l6-12h-8zM40 10h18v18l-8 12h-8l6-12h-8z" fill="#1cc36b"/></svg>
<p class="abs quote-text">The structured approach of this app has completely changed how I reflect on my days. It's amazing to see my progress and identify patterns in my behavior. I love how easy it is to capture my thoughts and see the positive changes over time. The app's intuitive design makes journaling a seamless part of my daily routine. The upcoming AI Coach is going to be a game-changer! I'm excited to get personalized insights and recommendations based on my journal entries.</p>
<div class="abs divider"></div>
<div class="abs avatar" role="img" aria-label="Portrait photo of the reviewer"></div>
<div class="abs who"><b>Elias Marrow</b><span>Development director</span></div>
<div class="abs pager">
  <svg width="34" height="10" viewBox="0 0 34 10" fill="none" stroke="#333"><path d="M33 5H2M6 1L2 5l4 4"/></svg>
  <span class="cur">01</span><svg width="16" height="40" viewBox="0 0 16 40"><path d="M14 2L2 38" stroke="#bbb"/></svg><span class="tot">04</span>
  <svg width="34" height="10" viewBox="0 0 34 10" fill="none" stroke="#333"><path d="M1 5h31M28 1l4 4-4 4"/></svg>
</div>

<!-- FAQ -->
<h2 class="abs sec-title" style="top:3429px">Frequently Asked <span class="accent">Questions</span></h2>
<p class="abs sec-sub" style="top:3483px">Find quick answers to your most common questions and get the most out of our journaling app.</p>
<div class="abs faq">
  <div>What is the purpose of this journaling app?</div><div>Is my data secure?</div>
  <div>How does the AI Coach work?</div><div>How can I provide feedback or suggest new features?</div>
  <div>Is the AI Coach available now?</div><div>What if I forget my password?</div>
  <div>What is the purpose of this journaling app?</div><div>How can I contact customer support?</div>
  <div>Can I use the app on multiple devices?</div><div>How often should I use the app for the best results?</div>
</div>

<!-- CTA -->
<section class="abs cta">
  <p class="eb">CONATC US</p>
  <h2>Start Your Reflection <b>Journey Today</b></h2>
  <p>Sign Up Now and Begin Transforming Your Insights into Action! Join our community and take the first step towards meaningful personal growth with daily reflections and actionable insights.</p>
  <span class="btn">Start Your Journey</span>
</section>

<!-- Footer -->
<footer>
  <div class="abs brand" style="left:185px;top:4160px"><span class="mark"></span>Tavorly</div>
  <p class="abs copy">Copyrights 2024. All Rights Reserved</p>
  <div class="abs social" aria-label="Social links"><i></i><i></i><i></i><i></i><i></i></div>
</footer>

</body>
</html>
```